Redo our website for our Robotics company

We sell robotic equipment to the restaurant industry. Our current robot, is a cooking robot that cooks up to 15 lbs of food. We will provide a prior website as well as brand guidelines. We plan on using wordpress and take advantage of wordpress's visual (no code) editor.

Current website - https://kelvatrix88.com/ (please note we are only selling Duffle now and no longer selling Pando+

We want someone to take our existing content and design the website as well as layout our content we provide. Here's a suggested site layout:

✅ KelvaTrix88 Website Wireframe / Site Map
1. Home

Purpose: Introduce Duffle, establish credibility, drive demo requests.

Sections:

Hero Section

Headline: “Meet Duffle — Your New Robotic Chef for High-Volume, Consistent Cooking.”

Sub-headline: Increase throughput. Reduce labor. Deliver perfect food every time.

CTA: Request a Demo + Watch Duffle Cook

Visual: Video loop or hero animation of Duffle in action.

How Duffle Works (3-4 steps)

Step cards: Load Ingredients → Select Recipe → Duffle Cooks → Serve

Icons and short explanations.

Key Benefits

Labor savings

Zero inconsistency

24/7 uptime

Throughput increases (30–50% faster)

Health & safety compliance

Who It’s For

QSR restaurants

Fast casual

Catering/commissaries

Ghost kitchens

Case Studies / Testimonials

Logo bar + quotes

“Duffle helped us reduce cooking times by 40%.”

Video Section

“Watch Duffle cook a full batch from start to finish.”

CTA Section

Big banner: Book a Demo

2. Product: “Meet Duffle”

Purpose: Deep dive into hardware, software, safety, reliability.

Sections:

Overview

What Duffle is

What tasks it automates

Where it fits in a kitchen

Hardware Features

High-temperature cooking chamber

Precision sensors

Automated stirring

Automated dispensing

Safety mechanisms (locking lids, auto-shutoff)

Software & AI

Recipe automation

IoT dashboard

Remote monitoring

Predictive maintenance

Specs Table

Dimensions

Power requirements

Capacity (lbs per batch)

Safety certifications

Gallery

Close-ups, installation photos, process shots

CTA: Request a Demo

3. Solutions

Purpose: Show that Duffle solves real operational problems.

Sub-pages or sections:

For Quick-Service Restaurants

Reduce labor cost

Speed up peak-hour demand

For Catering & Commissaries

Large-batch consistency

Automate repetitive cooking tasks

For High-Growth Chains

Replicable quality across multiple locations

Centralized recipe control

Each solution page includes:

A problem statement

How Duffle solves it

Metrics / KPIs

Relevant testimonial

CTA

4. ROI / Economics

Purpose: Sell the financial story clearly.

Sections:

Savings Calculator

Labor hours saved

Cost savings

Throughput increases

Food waste reduction

Before & After Comparison

Traditional kitchen vs. robotic kitchen

Sample ROI

“Payback in as little as 3–6 months.”

Download Full ROI Report (PDF)

5. Case Studies

Purpose: Social proof + real results.

Structure for each case study:

Customer background

Problem

Implementation

KPIs achieved

Labor savings

Consistency improvements

Cooking speed

Quote + photos/video

6. Pricing

Purpose: Start a commercial conversation.

Include:

Subscription model (monthly / annual)

Hardware leasing or purchase options

Installation + training

Support level

CTA to book a sales call

7. About

Purpose: Build trust.

Sections:

Mission statement

Founding team

Advisors/partners

“Why we built Duffle”

8. Resources

Purpose: SEO + education.

Subpages:

Blog (e.g., “The Future of Automated Kitchens”)

Whitepapers

Technical documentation

Product videos

9. Contact

General inquiry form

Sales contact

Support portal

Careers

```html
<!DOCTYPE html>
<html lang="en">
<head>
<meta charset="utf-8">
<title>KelvaTrix88 — Meet Duffle</title>
<link href="https://fonts.googleapis.com/css2?family=Roboto:wght@400;500;700;900&display=swap" rel="stylesheet">
<style>
:root{
  --brand:#f0442a;
  --brand-dark:#d8361f;
  --ink:#1d1d1f;
  --muted:#6b6b70;
  --navy:#1f2a44;
  --dark:#1a1a1c;
  --line:#e6e6e8;
  --white:#ffffff;
}
*{box-sizing:border-box;margin:0;padding:0}
html,body{width:1200px;height:4183px;overflow:hidden}
body{position:relative;background:var(--white);font-family:"Roboto",Arial,sans-serif;color:var(--ink)}
.abs{position:absolute}

/* hero */
.hero{left:0;top:0;width:1200px;height:637px;border-bottom-left-radius:120px;overflow:hidden;
  background:linear-gradient(180deg,#2a2a2c 0%,#1e1e20 60%,#151516 100%)}
.hero-photo{position:absolute;inset:0;background:radial-gradient(ellipse at 50% 40%,rgba(120,120,125,.35),rgba(0,0,0,0) 70%)}
.nav{position:absolute;top:46px;left:0;width:1200px;height:24px;font-size:14px;font-weight:500;color:var(--white)}
.nav a{position:absolute;color:var(--white);text-decoration:none;top:3px}
.nav .active{background:var(--brand);padding:3px 10px;top:0;transform:skewX(-12deg)}
.nav .active span{display:inline-block;transform:skewX(12deg)}
.logo{font-weight:900;color:var(--brand);letter-spacing:-.3px;display:flex;align-items:center;gap:8px}
.logo i{display:inline-block;background:var(--brand);border-radius:50%}
.nav .logo{position:absolute;left:516px;top:-2px;font-size:24px}
.nav .logo i{width:12px;height:12px}
.play{position:absolute;width:58px;height:58px;border:3px solid var(--brand);border-radius:50%}
.play:after{content:"";position:absolute;left:22px;top:15px;border-left:16px solid var(--brand);border-top:11px solid transparent;border-bottom:11px solid transparent}
.hero h1{position:absolute;top:276px;left:0;width:1200px;text-align:center;font-size:44px;line-height:52px;font-weight:500;color:var(--white)}
.hero h1 b{color:var(--brand);font-weight:900}
.hero .sub{position:absolute;top:402px;width:1200px;text-align:center;font-size:14px;color:var(--white)}
.btn{position:absolute;height:38px;display:flex;align-items:center;justify-content:center;gap:6px;font-size:13px;font-weight:500;color:var(--white);border-radius:4px;background:var(--brand)}
.btn.outline{background:transparent;border:1.5px solid var(--brand)}

/* section titles */
.title{position:absolute;left:0;width:1200px;display:flex;justify-content:center;align-items:center;gap:12px;font-size:34px;font-weight:500}
.tag{display:inline-block;background:var(--brand);color:var(--white);font-weight:700;padding:2px 18px;transform:skewX(-14deg);border-radius:6px 2px 6px 2px}
.tag span{display:inline-block;transform:skewX(14deg)}

/* cards */
.card{position:absolute;width:234px;background:var(--white);border-radius:10px;box-shadow:0 4px 14px rgba(0,0,0,.12);overflow:hidden}
.card .ph{height:227px;width:100%}
.card .name{position:absolute;left:19px;font-size:16px;font-weight:700;color:var(--ink)}
.card .dot{position:absolute;right:18px;width:16px;height:16px;border-radius:50%;background:var(--brand)}
.card .dot:after{content:"";position:absolute;left:6px;top:4px;border-left:5px solid #fff;border-top:4px solid transparent;border-bottom:4px solid transparent}
.card p{position:absolute;left:23px;top:275px;width:180px;font-size:12px;line-height:16px;color:var(--muted)}

/* benefits */
.ring{left:431px;top:1357px;width:340px;height:340px;border-radius:50%;border:3px solid #c9c9cc}
.ring .ph{position:absolute;left:18px;top:18px;width:298px;height:298px;border-radius:50%;background:radial-gradient(circle at 50% 45%,#8a8a8f,#3a3a3d 70%)}
.bicon{position:absolute;width:66px;height:66px;border-radius:50%;background:var(--brand);border:4px solid var(--white);box-shadow:0 2px 8px rgba(0,0,0,.15)}
.bicon svg{position:absolute;left:14px;top:14px}
.benefit{position:absolute;width:330px;font-size:15px;line-height:25px;color:var(--muted)}
.benefit h3{font-size:18px;font-weight:500;color:var(--navy);margin-bottom:2px}
.benefit.l{text-align:right}
.benefit.c{text-align:center}

/* who */
.who{left:0;top:1939px;width:1200px;height:604px;border-bottom-right-radius:120px;background:linear-gradient(180deg,#262628,#1c1c1e)}
.who .title{color:var(--white)}

/* testimonial */
.tcard{left:206px;top:2733px;width:775px;height:271px;border-radius:140px;background:var(--white);box-shadow:0 6px 22px rgba(0,0,0,.1)}
.tcard .ph{position:absolute;left:23px;top:15px;width:244px;height:244px;border-radius:50%;background:radial-gradient(circle at 40% 40%,#c65a3a,#3b2a24 75%)}
.stars{position:absolute;left:307px;top:57px;color:var(--brand);font-size:20px;letter-spacing:2px}
.quote{position:absolute;left:307px;top:92px;font-size:27px;line-height:37px;font-weight:700;color:var(--ink)}
.client{position:absolute;left:307px;top:175px;font-size:44px;font-weight:500;color:var(--brand)}
.arrow{position:absolute;width:20px;height:34px}

/* video */
.video{left:0;top:3142px;width:1200px;height:577px;border-bottom-left-radius:130px;background:linear-gradient(135deg,#3a4150,#23262c 55%,#1a1b1e)}
.video h2{position:absolute;top:3472px;width:1200px;text-align:center;font-size:26px;font-weight:700;color:var(--white)}

/* footer */
.foot h4{position:absolute;font-size:16px;font-weight:700;color:var(--ink)}
.flist{position:absolute;font-size:14px;line-height:22px;color:var(--muted);list-style:none}
.social li,.hello li{display:flex;align-items:center;gap:10px;margin-bottom:12px}
.ci{width:14px;height:14px;border-radius:50%;border:1.5px solid var(--brand);flex:none}
.input{left:110px;top:3954px;width:310px;height:44px;border:1px solid #d8d8dc;border-radius:4px;font-size:13px;color:#9a9aa0;padding:14px 16px}
.rule{left:110px;top:4109px;width:976px;height:1px;background:var(--line)}
.legal{position:absolute;top:4138px;font-size:13px;color:var(--muted)}
</style>
</head>
<body>

<section class="abs hero">
  <div class="hero-photo" role="img" aria-label="Row of Duffle cooking robots in a commercial kitchen"></div>
  <nav class="nav">
    <a class="active" style="left:104px"><span>Home</span></a>
    <a style="left:174px">Meet Duffle</a>
    <a style="left:275px">Solutions</a>
    <a style="left:359px">ROI / Economics</a>
    <div class="logo"><i></i>KelvaTrix88</div>
    <a style="left:700px">Case Studies</a>
    <a style="left:810px">Pricing</a>
    <a style="left:877px">About</a>
    <a style="left:938px">Resources</a>
    <a style="left:1030px">Contact</a>
  </nav>
  <div class="play" style="left:571px;top:185px"></div>
  <h1><b>Meet Duffle</b> Your New Robotic Chef for<br>High-Volume, Consistent Cooking.</h1>
  <p class="sub">Increase throughput. Reduce labor. Deliver perfect food every time.</p>
  <div class="btn outline" style="left:405px;top:450px;width:170px">Request a Demo ➞</div>
  <div class="btn" style="left:596px;top:450px;width:200px">Watch Duffle Cook ➞</div>
</section>

<div class="title" style="top:724px"><span class="tag"><span>How</span></span>Duffle Works</div>
<div class="card" style="left:110px;top:810px;height:278px"><div class="ph" role="img" aria-label="Bowls of spices, salmon and roe" style="background:linear-gradient(135deg,#c2542e,#5a1e14)"></div><div class="name" style="top:242px">Load Ingredients</div><div class="dot" style="top:245px"></div></div>
<div class="card" style="left:359px;top:810px;height:351px"><div class="ph" role="img" aria-label="Tablet showing a recipe beside fresh vegetables" style="background:linear-gradient(135deg,#e9e6df,#9aa68a)"></div><div class="name" style="top:242px">Select Recipe</div><p>Lorem ipsum dolor sit amet, consectetur adipiscing elit, sed do eiusmod tempor</p></div>
<div class="card" style="left:607px;top:810px;height:278px"><div class="ph" role="img" aria-label="Duffle cooking robots in a row" style="background:linear-gradient(180deg,#6e6e73,#2e2e31)"></div><div class="name" style="top:242px">Duffle Cooks</div><div class="dot" style="top:245px"></div></div>
<div class="card" style="left:856px;top:810px;height:278px"><div class="ph" role="img" aria-label="Kitchen worker serving a plated meal" style="background:linear-gradient(135deg,#b8a68e,#c7652a)"></div><div class="name" style="top:242px">Serve</div><div class="dot" style="top:245px"></div></div>

<div class="title" style="top:1259px"><span class="tag"><span>Key</span></span>Benefits</div>
<div class="abs ring"><div class="ph" role="img" aria-label="Duffle cooking robot units"></div></div>
<div class="bicon" style="left:437px;top:1410px"><svg width="30" height="30" viewBox="0 0 30 30" fill="none" stroke="#fff" stroke-width="2"><circle cx="15" cy="11" r="6"/><path d="M5 27c2-6 18-6 20 0"/></svg></div>
<div class="bicon" style="left:708px;top:1410px"><svg width="30" height="30" viewBox="0 0 30 30" fill="none" stroke="#fff" stroke-width="2"><path d="M4 25L14 13l5 5 8-12"/><path d="M21 6h6v6"/></svg></div>
<div class="bicon" style="left:437px;top:1558px"><svg width="30" height="30" viewBox="0 0 30 30" fill="none" stroke="#fff" stroke-width="2"><rect x="6" y="4" width="18" height="23" rx="2"/><path d="M10 12h10M10 17h10M10 22h6"/></svg></div>
<div class="bicon" style="left:708px;top:1558px"><svg width="30" height="30" viewBox="0 0 30 30" fill="none" stroke="#fff" stroke-width="2"><path d="M15 3l10 4v8c0 6-5 10-10 12C10 25 5 21 5 15V7z"/><path d="M10 15l4 4 6-7"/></svg></div>
<div class="bicon" style="left:567px;top:1656px"><svg width="30" height="30" viewBox="0 0 30 30" fill="none" stroke="#fff" stroke-width="2"><circle cx="15" cy="15" r="11"/><path d="M15 8v7l5 3"/></svg></div>
<div class="benefit l" style="left:81px;top:1401px"><h3>Labor savings</h3>Lorem ipsum dolor sit amet, consectetur adipiscing elit, sed do eiusmod tempor</div>
<div class="benefit l" style="left:74px;top:1552px"><h3>Zero inconsistency</h3>Lorem ipsum dolor sit amet, consectetur adipiscing elit, sed do eiusmod tempor</div>
<div class="benefit" style="left:794px;top:1402px;width:360px"><h3>Throughput increases (30–50% faster)</h3>Lorem ipsum dolor sit amet, consectetur adipiscing elit, sed do eiusmod tempor</div>
<div class="benefit" style="left:796px;top:1552px"><h3>Health &amp; safety compliance</h3>Lorem ipsum dolor sit amet, consectetur adipiscing elit, sed do eiusmod tempor</div>
<div class="benefit c" style="left:434px;top:1756px"><h3>24/7 uptime</h3>Lorem ipsum dolor sit amet, consectetur adipiscing elit, sed do eiusmod tempor</div>

<section class="abs who" role="img" aria-label="Dimmed kitchen with Duffle robots in the background">
  <div class="title" style="top:68px"><span class="tag"><span>Who</span></span>It’s For</div>
</section>
<div class="card" style="left:110px;top:2134px;height:278px"><div class="ph" role="img" aria-label="Quick-service restaurant dining room" style="background:linear-gradient(135deg,#c08a4a,#4a3320)"></div><div class="name" style="top:242px">QSR restaurants</div><div class="dot" style="top:245px"></div></div>
<div class="card" style="left:359px;top:2134px;height:278px"><div class="ph" role="img" aria-label="Fast casual kitchen staff at the counter" style="background:linear-gradient(135deg,#d9cbb5,#2a2a2c)"></div><div class="name" style="top:242px">Fast Casual</div><div class="dot" style="top:245px"></div></div>
<div class="card" style="left:607px;top:2134px;height:278px"><div class="ph" role="img" aria-label="Catering trays of prepared food" style="background:linear-gradient(135deg,#b9bcc2,#8a6a3e)"></div><div class="name" style="top:242px">Catering</div><div class="dot" style="top:245px"></div></div>
<div class="card" style="left:856px;top:2134px;height:278px"><div class="ph" role="img" aria-label="Compact ghost kitchen interior" style="background:linear-gradient(135deg,#e4e1dc,#6b5a48)"></div><div class="name" style="top:242px">Ghost kitchens</div><div class="dot" style="top:245px"></div></div>

<div class="title" style="top:2630px"><span class="tag"><span>Our</span></span>Testimonials</div>
<svg class="arrow" style="left:144px;top:2851px" viewBox="0 0 20 34"><path d="M16 3L4 17l12 14" fill="none" stroke="var(--brand)" stroke-width="4"/></svg>
<div class="abs tcard">
  <div class="ph" role="img" aria-label="Duffle robot with bowls of cooked dishes"></div>
  <div class="stars">★★★★★</div>
  <div class="quote">Duffle helped us reduce<br>cooking times by 40%</div>
  <div class="client">Ornelo</div>
</div>
<svg class="arrow" style="left:1022px;top:2851px" viewBox="0 0 20 34"><path d="M4 3l12 14L4 31" fill="none" stroke="var(--brand)" stroke-width="4"/></svg>

<section class="abs video" role="img" aria-label="Team demonstrating Duffle at a trade show booth"></section>
<div class="play" style="left:571px;top:3366px"></div>
<div class="video"><h2 style="position:absolute;top:3472px;width:1200px;text-align:center;font-size:26px;font-weight:700;color:#fff">Watch Duffle cook a full batch from start to finish</h2></div>
<div class="btn" style="left:515px;top:3540px;width:170px">Book a Demo ➞</div>

<footer class="foot">
  <div class="abs logo" style="left:110px;top:3814px;font-size:40px"><i style="width:18px;height:18px"></i>KelvaTrix88</div>
  <h4 style="left:110px;top:3910px">Newsletter Signup</h4>
  <div class="abs input">Your email</div>
  <div class="btn" style="left:114px;top:4026px;width:118px;height:40px">Submit ➞</div>

  <h4 style="left:486px;top:3828px">Socials</h4>
  <ul class="flist social" style="left:486px;top:3870px">
    <li><span class="ci"></span>KelvaTrix88</li>
    <li><span class="ci"></span>@KelvaTrix88</li>
    <li><span class="ci"></span>@KelvaTrix88</li>
  </ul>

  <h4 style="left:693px;top:3828px">Menu</h4>
  <ul class="flist" style="left:693px;top:3872px">
    <li>Home</li><li>Meet Duffle</li><li>Solutions</li><li>ROI / Economics</li><li>Case Studies</li><li>Pricing</li><li>About</li><li>Resources</li><li>Contact</li>
  </ul>

  <h4 style="left:872px;top:3828px">Say Hello</h4>
  <ul class="flist hello" style="left:872px;top:3870px">
    <li><svg width="16" height="12" viewBox="0 0 16 12" fill="none" stroke="var(--brand)" stroke-width="1.5"><rect x="1" y="1" width="14" height="10"/><path d="M1 1l7 6 7-6"/></svg>info@kelvatrix88.com</li>
    <li><svg width="16" height="16" viewBox="0 0 16 16"><path d="M3 1l3 3-2 2c1 2 3 4 5 5l2-2 3 3-2 3C7 14 2 9 1 3z" fill="var(--brand)"/></svg>+1 [877] 555 0142</li>
  </ul>

  <div class="abs rule"></div>
  <p class="legal" style="left:110px">KelvaTrix88©2025. All Rights Reserved.</p>
  <p class="legal" style="left:876px">Privacy Policy &nbsp;|| Terms of Service</p>
</footer>

</body>
</html>
```